Attention grabbing 6x9 postcard

We are looking to have an attention grabbing post card that be sent out to homeowners from our roofing company Olum Roofing. the concept is that on the front it will say something like (STOP THE KNOCKING!
Tired of roofers knocking on your door? Contact us because we value your time as much as you value the roof over your head."
Olum Roofing
OlumRoofing.com
877.612.OLUM
info@olumroofing.com

Please feel free to come up with something very creative. Once we pick the final design we will provide the copy.

```html
<!DOCTYPE html>
<html lang="en">
<head>
<meta charset="utf-8">
<title>Olum Roofing Postcard</title>
<link href="https://fonts.googleapis.com/css2?family=Antonio:wght@700&family=Jost:wght@400;500;600&family=Montserrat:wght@800&display=swap" rel="stylesheet">
<style>
  :root{
    --stage:#2e2d3c;
    --gold:#e0a526;
    --silver:#e4e4e4;
    --brown:#4a1a0c;
    --panel:#2a2626;
    --ink:#141414;
    --white:#ffffff;
    --rule:#8a8a8a;
  }
  *{margin:0;padding:0;box-sizing:border-box}
  html,body{width:933px;height:1200px;overflow:hidden;background:var(--stage)}
  .card{position:absolute;left:87px;width:759px;height:506px;background:var(--white);overflow:hidden;font-family:"Jost",sans-serif}
  .card--front{top:75px}
  .card--back{top:620px}
  .layer{position:absolute;left:0;top:0}
  .abs{position:absolute}

  .headline{position:absolute;font-family:"Antonio",sans-serif;font-weight:700;font-size:96px;line-height:1;letter-spacing:-1px;white-space:nowrap}
  .headline--top{right:474px;top:118px;color:var(--silver);transform:scaleX(.88);transform-origin:right top}
  .headline--bottom{left:33px;top:209px;color:var(--gold);transform:scaleX(.88);transform-origin:left top}

  .tab{position:absolute;left:0;background:var(--gold);font-family:"Montserrat",sans-serif;font-weight:800;color:var(--ink);display:flex;align-items:center;white-space:nowrap;box-shadow:3px 0 0 0 var(--white),5px 0 0 0 var(--gold)}
  .tab--services{top:322px;height:22px;width:127px;padding-left:34px;font-size:16.5px}
  .tab--process{top:74px;height:23px;width:196px;padding-left:34px;font-size:11.5px}

  .service-list{position:absolute;left:34px;top:350px;list-style:none;color:var(--white);font-size:11.8px;letter-spacing:.2px}
  .service-list li{height:20px;display:flex;align-items:center;gap:4px;white-space:nowrap}
  .tick{width:7px;height:7px;flex:none}

  .phone{position:absolute;display:flex;align-items:center;height:30px}
  .phone-icon{position:absolute;left:0;top:5px}
  .phone-number{position:absolute;left:21px;top:0;font-family:"Antonio",sans-serif;font-weight:700;color:var(--ink);font-size:27px;line-height:30px;white-space:nowrap;transform:scaleX(.8);transform-origin:left center}

  .contact{position:absolute;left:216px;font-size:13.5px;color:var(--ink);line-height:17px;white-space:nowrap}
  .contact div{display:flex;align-items:center;gap:5px}
  .contact .web{font-weight:600}

  .intro{left:34px;top:13px;color:var(--gold);font-size:12.8px;white-space:nowrap}
  .back-title{left:34px;top:33px;font-family:"Montserrat",sans-serif;font-weight:800;color:var(--white);font-size:27px;line-height:1;letter-spacing:-.3px;white-space:nowrap}
  .process{position:absolute;left:35px;top:104px;width:330px;list-style:none;color:var(--white);font-size:9.4px;line-height:11.4px}
  .process li{margin-bottom:4px;padding-left:12px;text-indent:-12px}
  .process b{color:var(--gold);font-weight:500;margin-right:3px}

  .why-title{left:28px;top:346px;font-family:"Montserrat",sans-serif;font-weight:800;font-size:19px;letter-spacing:-.2px;color:var(--ink);white-space:nowrap}
  .why-grid{position:absolute;left:27px;top:375px;display:grid;grid-template-columns:131px 200px;row-gap:5px;font-size:12px;font-weight:500;color:var(--ink)}
  .why-grid span{display:flex;align-items:center;gap:7px;height:18px;white-space:nowrap}

  .back-name{left:469px;top:58px;font-size:20px;font-weight:600;color:var(--gold);white-space:nowrap}
  .stamp{left:651px;top:26px;width:80px;height:66px;background:#444}
  .address-line{position:absolute;left:469px;width:262px;height:1px;background:var(--rule)}
</style>
</head>
<body>

<section class="card card--front">
  <svg class="layer" width="759" height="506" viewBox="0 0 759 506">
    <defs>
      <clipPath id="bigHex"><polygon points="602,46 778,148 778,351 602,452 426,351 426,148"/></clipPath>
      <clipPath id="smallHex"><polygon points="414,263 499,313 499,411 414,459 329,411 329,313"/></clipPath>
      <linearGradient id="roofPhoto" x1="0" y1="0" x2="1" y2="1">
        <stop offset="0" stop-color="#8a8a8c"/><stop offset=".6" stop-color="#6f6d6c"/><stop offset="1" stop-color="#545250"/>
      </linearGradient>
      <linearGradient id="housePhoto" x1="0" y1="0" x2="0" y2="1">
        <stop offset="0" stop-color="#3c6fc8"/><stop offset=".35" stop-color="#5d5650"/><stop offset=".6" stop-color="#a8865c"/><stop offset="1" stop-color="#7a5e3e"/>
      </linearGradient>
    </defs>
    <polygon fill="var(--panel)" points="14,99 440,99 381,133 381,305 312,345 312,441 14,441"/>
    <polyline fill="none" stroke="var(--brown)" stroke-width="11" points="392,345 392,130 420,114"/>
    <polyline fill="none" stroke="var(--brown)" stroke-width="11" points="473,39 492,39 492,84 602,18 770,115"/>
    <polygon fill="none" stroke="var(--brown)" stroke-width="14" points="414,250 511,306 511,418 414,474 317,418 317,306"/>
    <polyline fill="none" stroke="var(--brown)" stroke-width="11" points="759,260 688,301 688,408 759,446"/>
    <polyline fill="none" stroke="var(--brown)" stroke-width="11" points="530,512 602,466 680,512"/>
    <g clip-path="url(#bigHex)"><rect role="img" aria-label="Photo of a roofer nailing shingles" x="420" y="40" width="360" height="420" fill="url(#roofPhoto)"/></g>
    <g clip-path="url(#smallHex)"><rect role="img" aria-label="Photo of a new house under construction" x="320" y="258" width="190" height="206" fill="url(#housePhoto)"/></g>
    <polygon fill="var(--gold)" points="0,456 168,456 198,506 0,506"/>
    <line x1="174" y1="456" x2="204" y2="506" stroke="#b9b9b9" stroke-width="3"/>
    <polygon fill="var(--gold)" points="198,498 520,498 515,506 204,506"/>
  </svg>

  <div class="headline headline--top">OLUM</div>
  <div class="headline headline--bottom">ROOFING</div>

  <div class="tab tab--services">SERVICES</div>
  <ul class="service-list">
    <li><svg class="tick" viewBox="0 0 10 10"><circle cx="5" cy="5" r="4" fill="none" stroke="var(--gold)" stroke-width="1.2"/><path d="M3 5l1.5 1.5L7.5 3.5" fill="none" stroke="var(--gold)" stroke-width="1.2"/></svg>RETAIL/COMMERCIAL ROOF REPLACEMENT</li>
    <li><svg class="tick" viewBox="0 0 10 10"><circle cx="5" cy="5" r="4" fill="none" stroke="var(--gold)" stroke-width="1.2"/><path d="M3 5l1.5 1.5L7.5 3.5" fill="none" stroke="var(--gold)" stroke-width="1.2"/></svg>STORM DAMAGE ROOF REPLACEMENT</li>
    <li><svg class="tick" viewBox="0 0 10 10"><circle cx="5" cy="5" r="4" fill="none" stroke="var(--gold)" stroke-width="1.2"/><path d="M3 5l1.5 1.5L7.5 3.5" fill="none" stroke="var(--gold)" stroke-width="1.2"/></svg>NEW CONSTRUCTION</li>
    <li><svg class="tick" viewBox="0 0 10 10"><circle cx="5" cy="5" r="4" fill="none" stroke="var(--gold)" stroke-width="1.2"/><path d="M3 5l1.5 1.5L7.5 3.5" fill="none" stroke="var(--gold)" stroke-width="1.2"/></svg>REPAIRS &amp; RESTORATION</li>
  </ul>

  <div class="phone" style="left:35px;top:466px">
    <svg class="phone-icon" width="14" height="20" viewBox="0 0 14 20"><rect x="2" y="1" width="10" height="18" rx="2" fill="none" stroke="var(--ink)" stroke-width="1.4"/><line x1="5.5" y1="16" x2="8.5" y2="16" stroke="var(--ink)" stroke-width="1.4"/></svg>
    <span class="phone-number">877.612.OLUM</span>
  </div>
  <div class="contact" style="top:458px">
    <div class="web"><svg width="12" height="12" viewBox="0 0 12 12"><circle cx="6" cy="6" r="5" fill="none" stroke="var(--ink)"/><ellipse cx="6" cy="6" rx="2.2" ry="5" fill="none" stroke="var(--ink)"/><line x1="1" y1="6" x2="11" y2="6" stroke="var(--ink)"/></svg>OlumRoofing.com</div>
    <div><svg width="12" height="10" viewBox="0 0 12 10"><rect x=".5" y=".5" width="11" height="9" fill="none" stroke="var(--ink)"/><path d="M.5 .5L6 5.5 11.5 .5" fill="none" stroke="var(--ink)"/></svg>info@olumroofing.com</div>
  </div>
</section>

<section class="card card--back">
  <svg class="layer" width="759" height="506" viewBox="0 0 759 506">
    <defs>
      <linearGradient id="skyFade" x1="0" y1="0" x2="0" y2="1">
        <stop offset="0" stop-color="#9fd6e3"/><stop offset=".7" stop-color="#e4f4f3"/><stop offset="1" stop-color="#cfe6e4"/>
      </linearGradient>
      <linearGradient id="housePhotoDark" x1="0" y1="0" x2="0" y2="1">
        <stop offset="0" stop-color="#2b1c15"/><stop offset=".6" stop-color="#3b2419"/><stop offset="1" stop-color="#2a1912"/>
      </linearGradient>
      <clipPath id="hexA"><polygon points="88,198 137,226 137,282 88,310 39,282 39,226"/></clipPath>
      <clipPath id="hexB"><polygon points="209,226 258,254 258,310 209,338 160,310 160,254"/></clipPath>
      <clipPath id="hexC"><polygon points="329,198 378,226 378,282 329,310 280,282 280,226"/></clipPath>
    </defs>
    <rect role="img" aria-label="Soft misty hills behind a pale sky" x="0" y="0" width="404" height="506" fill="url(#skyFade)"/>
    <polygon role="img" aria-label="Darkened photo of a house roof" fill="url(#housePhotoDark)" points="19,0 386,0 386,202 300,250 209,224 120,250 19,202"/>
    <g clip-path="url(#hexA)"><rect role="img" aria-label="Close-up photo of roof shingles" x="35" y="195" width="110" height="120" fill="#5e6066"/></g>
    <g clip-path="url(#hexB)"><rect role="img" aria-label="Photo of a house with new roof and dormers" x="155" y="222" width="110" height="120" fill="#7d8275"/></g>
    <g clip-path="url(#hexC)"><rect role="img" aria-label="Photo of a finished roof among trees" x="275" y="195" width="110" height="120" fill="#8a9186"/></g>
    <g fill="none" stroke="var(--white)" stroke-width="3">
      <polygon points="88,198 137,226 137,282 88,310 39,282 39,226"/>
      <polygon points="209,226 258,254 258,310 209,338 160,310 160,254"/>
      <polygon points="329,198 378,226 378,282 329,310 280,282 280,226"/>
    </g>
    <circle cx="258" cy="360" r="2" fill="var(--gold)"/>
    <polyline fill="none" stroke="#555" stroke-width=".8" points="263,360 377,360 377,414"/>
    <polygon fill="var(--gold)" points="0,455 170,455 199,499 0,499"/>
    <line x1="176" y1="455" x2="205" y2="499" stroke="#b9b9b9" stroke-width="3"/>
    <rect fill="var(--gold)" x="0" y="499" width="759" height="7"/>
  </svg>

  <p class="intro abs">You worked hard building your home.</p>
  <h1 class="back-title abs">PROTECT YOUR HOME!</h1>
  <div class="tab tab--process">OLUM ROOFING PROCESS</div>
  <ol class="process">
    <li><b>1.</b>Complementary consultation to access your roofing needs and review our honest recommendations.</li>
    <li><b>2.</b>Our team of professionals replace, restore, or repair your roof making the process as stress-free as possible.</li>
    <li><b>3.</b>100% satisfaction, peace of mind, and continued professional coverage backed by OLUM Protection*.</li>
  </ol>

  <h2 class="why-title abs">WHY CHOOSE OLUM?</h2>
  <div class="why-grid">
    <span><svg width="10" height="10" viewBox="0 0 10 10"><circle cx="5" cy="5" r="4" fill="none" stroke="var(--ink)" stroke-width=".9"/><path d="M3 5l1.5 1.5L8.5 2" fill="none" stroke="var(--ink)" stroke-width=".9"/></svg>LOCAL</span>
    <span><svg width="10" height="10" viewBox="0 0 10 10"><circle cx="5" cy="5" r="4" fill="none" stroke="var(--ink)" stroke-width=".9"/><path d="M3 5l1.5 1.5L8.5 2" fill="none" stroke="var(--ink)" stroke-width=".9"/></svg>COMMUNITY DRIVEN</span>
    <span><svg width="10" height="10" viewBox="0 0 10 10"><circle cx="5" cy="5" r="4" fill="none" stroke="var(--ink)" stroke-width=".9"/><path d="M3 5l1.5 1.5L8.5 2" fill="none" stroke="var(--ink)" stroke-width=".9"/></svg>FAMILY-OWNED</span>
    <span><svg width="10" height="10" viewBox="0 0 10 10"><circle cx="5" cy="5" r="4" fill="none" stroke="var(--ink)" stroke-width=".9"/><path d="M3 5l1.5 1.5L8.5 2" fill="none" stroke="var(--ink)" stroke-width=".9"/></svg>ONGOING COMMUNICATION</span>
  </div>

  <div class="phone" style="left:28px;top:465px">
    <svg class="phone-icon" width="14" height="20" viewBox="0 0 14 20"><rect x="2" y="1" width="10" height="18" rx="2" fill="none" stroke="var(--ink)" stroke-width="1.4"/><line x1="5.5" y1="16" x2="8.5" y2="16" stroke="var(--ink)" stroke-width="1.4"/></svg>
    <span class="phone-number">877.612.OLUM</span>
  </div>
  <div class="contact" style="top:457px">
    <div class="web"><svg width="12" height="12" viewBox="0 0 12 12"><circle cx="6" cy="6" r="5" fill="none" stroke="var(--ink)"/><ellipse cx="6" cy="6" rx="2.2" ry="5" fill="none" stroke="var(--ink)"/><line x1="1" y1="6" x2="11" y2="6" stroke="var(--ink)"/></svg>OlumRoofing.com</div>
    <div><svg width="12" height="10" viewBox="0 0 12 10"><rect x=".5" y=".5" width="11" height="9" fill="none" stroke="var(--ink)"/><path d="M.5 .5L6 5.5 11.5 .5" fill="none" stroke="var(--ink)"/></svg>info@olumroofing.com</div>
  </div>

  <div class="back-name abs">Olum Roofing</div>
  <div class="stamp abs"></div>
  <div class="address-line" style="top:209px"></div>
  <div class="address-line" style="top:259px"></div>
  <div class="address-line" style="top:309px"></div>
  <div class="address-line" style="top:359px"></div>
</section>

</body>
</html>
```